Motel Sign - Front

(21/03/12 - I've edited the brief and removing the words "garden view" its not fitting in the designs I'm getting and just want the word motel to be the focus. I have a template/vision of what I want - see the whiteboard sketch of what I'm looking for uploaded today. Definitely open to creatively, new designs and different ideas but the whiteboard design I've done should be a guideline. Keep it fresh/green/white. use the sample photos of green as inspiration. Thanks)
We are a motel set in the mountain country of Victoria - Australia. The front of the motel needs a fresh look. We recently removed a large amount of the garden to expose a brick courtyard fence which the front of the courtyard faces out to the main road. Within the courtyard fence there is a wooden frame and paneling.
We want to have a new sign created to slot into the wooden frame. (see photo) its the white component.
Its a very large and unusual shape and I want to keep it simple but need to fill the in the best way possible.
The space is 940mm high and 4940mm width.
The message of the sign is simple the word "MOTEL". I want people to be able to drive past and glance in and see we are a motel straight away. So the main purpose of the sign is to say "MOTEL".
I am open to colour use to match the space and have impact. I thought a background colour should be 'off white'. I'm open to the colours used to match your design as long as it matches the brief. Maybe a garden green for the emblem.
IN BRIEF:
1) the word "MOTEL"
2) Border/Background that ties in the garden.
The design should be centred, clean and simple, doesn't have to fill the whole space as long as its balanced and centred.
I like cursive and garden like designs for this one - as long its the word MOTEL still has impact. (OPEN TO NEW IDEAS)
I am also open to different ideas and suggestions if you feel you have a better way to take advantage of this space.
The sign will be 7-8 metres from the road itself.
NOTE: the photos show the space and the painted white in the space where the sign will go. The garden in front of this space will be completely cleared.

```html
<!DOCTYPE html>
<html lang="en">
<head>
<meta charset="utf-8">
<title>Motel Sign – Front</title>
<link rel="stylesheet" href="https://fonts.googleapis.com/css2?family=Patua+One&display=swap">
<style>
  :root {
    --canvas-white: #ffffff;
    --garden-light: #b9dd84;
    --garden-mid: #8cc653;
    --garden-deep: #6db33f;
    --vine-green: #2f7d34;
    --vine-soft: #4f9a3a;
    --letter-white: #ffffff;
    --letter-shadow: #111111;
  }
  * { box-sizing: border-box; margin: 0; padding: 0; }
  html, body {
    width: 1200px;
    height: 785px;
    overflow: hidden;
    background: var(--canvas-white);
  }
  .sign-sheet {
    position: relative;
    width: 1200px;
    height: 785px;
    background: var(--canvas-white);
  }
  .sign-panel {
    position: absolute;
    left: 0;
    width: 1200px;
    height: 230px;
    overflow: hidden;
    background:
      radial-gradient(ellipse at 50% 40%, var(--garden-light) 0%, var(--garden-mid) 55%, var(--garden-deep) 100%);
  }
  .sign-panel--upper { top: 0; }
  .sign-panel--lower { top: 555px; }

  .vine-ornament {
    position: absolute;
    top: 0;
    height: 100%;
  }
  .vine-ornament--left {
    left: 0;
    width: 270px;
    background: linear-gradient(90deg, var(--vine-green) 0%, var(--vine-soft) 45%, rgba(79,154,58,0) 100%);
    opacity: 0.55;
  }
  .vine-ornament--right {
    right: 0;
    width: 270px;
    background: linear-gradient(270deg, var(--vine-green) 0%, var(--vine-soft) 45%, rgba(79,154,58,0) 100%);
    opacity: 0.55;
  }

  .sign-word {
    position: absolute;
    left: 0;
    right: 0;
    top: 50%;
    transform: translateY(-50%);
    text-align: center;
    font-family: "Patua One", serif;
    font-weight: 400;
    font-size: 250px;
    line-height: 1;
    letter-spacing: 2px;
    color: var(--letter-white);
    text-shadow: -7px 6px 0 var(--letter-shadow);
  }
</style>
</head>
<body>
  <main class="sign-sheet">
    <section class="sign-panel sign-panel--upper">
      <div class="vine-ornament vine-ornament--left" role="img" aria-label="Curling garden vine with leaves and small flowers"></div>
      <div class="vine-ornament vine-ornament--right" role="img" aria-label="Curling garden vine with leaves and small white flowers"></div>
      <h1 class="sign-word">MOTEL</h1>
    </section>

    <section class="sign-panel sign-panel--lower">
      <div class="vine-ornament vine-ornament--left" role="img" aria-label="Curling garden vine with leaves and small flowers"></div>
      <div class="vine-ornament vine-ornament--right" role="img" aria-label="Curling garden vine with leaves and small white flowers"></div>
      <p class="sign-word">MOTEL</p>
    </section>
  </main>
</body>
</html>
```